Author and Publisher

Cover for a book on the process of publishing a book from the presentation to the publisher until the selling in bookstores :
A behind-the-scenes journey through the world of book publishing, from manuscript to bookstore. The book explores the relationship between authors and publishers, manuscript selection, contracts, editing, proofreading, book design, printing, distribution, bookstores and online sales. It reveals the many people, decisions and processes involved in turning a text into a physical book and bringing it to readers. The illustration should evoke publishing as a lively, contemporary ecosystem, combining creativity, craftsmanship, business and the enduring appeal of books.
FORMAT : 14 x 20,5 cm
AUTHOR : Luc Varennes
TITLE : Le scribe et la presse
PUBLISHER : Editions Trovel (at the bottom of the page)
Target Market(s)
General public, mainly news authors of books
Look and feel
Each slider illustrates characteristics of the customer's brand and the style your logo design should communicate.

```html
<!DOCTYPE html>
<html lang="fr">
<head>
<meta charset="utf-8">
<title>Le scribe et la presse — Luc Varennes</title>
<link rel="stylesheet" href="https://fonts.googleapis.com/css2?family=Bodoni+Moda:wght@500;600&family=Saira:wght@400;500&display=swap">
<style>
  :root {
    --page-bg: #ffffff;
    --navy-deep: #04122f;
    --navy: #0a2a66;
    --royal: #0b47a3;
    --gold-light: #e0c07e;
    --gold: #c29a55;
    --gold-dark: #8d6a31;
    --cream: #e8d9b3;
    --stone-light: #c3cad6;
    --stone: #8b96a8;
    --stone-dark: #3d4b66;
  }
  * { margin: 0; padding: 0; box-sizing: border-box; }
  html, body {
    width: 1060px;
    height: 1200px;
    overflow: hidden;
    background: var(--page-bg);
  }
  .cover {
    position: absolute;
    left: 147px;
    top: 40px;
    width: 765px;
    height: 1120px;
    overflow: hidden;
    background: linear-gradient(180deg, var(--navy-deep) 0%, var(--navy) 30%, var(--royal) 58%, var(--royal) 100%);
    box-shadow: 0 18px 40px rgba(0, 0, 0, 0.25);
  }
  .cover__backdrop {
    position: absolute;
    left: 0;
    top: 0;
    width: 765px;
    height: 1120px;
  }
  .title {
    position: absolute;
    left: 0;
    width: 100%;
    text-align: center;
    font-family: 'Bodoni Moda', serif;
    font-weight: 600;
    background: linear-gradient(180deg, var(--gold-light) 0%, var(--gold) 50%, var(--gold-dark) 100%);
    -webkit-background-clip: text;
    background-clip: text;
    color: transparent;
    line-height: 1;
  }
  .title__line {
    font-size: 112px;
    letter-spacing: -3px;
  }
  .title__line--top { top: 58px; }
  .title__line--bottom { top: 262px; }
  .title__joiner {
    top: 176px;
    font-size: 68px;
    letter-spacing: -1px;
  }
  .title-rule {
    position: absolute;
    top: 214px;
    height: 3px;
    width: 180px;
    background: var(--gold);
  }
  .title-rule--left { left: 122px; }
  .title-rule--right { right: 128px; }
  .subtitle {
    position: absolute;
    left: 0;
    top: 392px;
    width: 100%;
    text-align: center;
    font-family: 'Saira', sans-serif;
    font-weight: 400;
    font-size: 21px;
    line-height: 34px;
    color: var(--gold-light);
  }
  .illustration {
    position: absolute;
    left: 122px;
    top: 505px;
    width: 515px;
    height: 465px;
    border-radius: 14px;
    background: radial-gradient(ellipse at 55% 40%, #3f66a8 0%, #1d3d78 45%, #14295a 80%, rgba(20, 41, 90, 0.6) 100%);
    transform: rotate(-8deg);
  }
  .credits {
    position: absolute;
    left: 0;
    width: 100%;
    text-align: center;
    font-family: 'Saira', sans-serif;
    color: var(--cream);
  }
  .author {
    top: 1014px;
    font-size: 34px;
    font-weight: 500;
    letter-spacing: 0.5px;
  }
  .author-rule {
    position: absolute;
    top: 1039px;
    height: 2px;
    width: 160px;
    background: var(--cream);
    opacity: 0.85;
  }
  .author-rule--left { left: 80px; }
  .author-rule--right { right: 80px; }
  .publisher {
    top: 1068px;
    font-size: 25px;
    font-weight: 500;
    letter-spacing: 16px;
    padding-left: 16px;
  }
</style>
</head>
<body>
  <main class="cover">
    <svg class="cover__backdrop" viewBox="0 0 765 1120" aria-hidden="true">
      <defs>
        <linearGradient id="stoneGradient" x1="0" y1="0" x2="0" y2="1">
          <stop offset="0" stop-color="var(--stone-light)"/>
          <stop offset="0.45" stop-color="var(--stone)"/>
          <stop offset="1" stop-color="var(--stone-dark)"/>
        </linearGradient>
      </defs>
      <circle cx="382" cy="1138" r="573" fill="url(#stoneGradient)"/>
    </svg>

    <h1 class="title title__line title__line--top">LE SCRIBE</h1>
    <span class="title-rule title-rule--left"></span>
    <span class="title title__joiner">et</span>
    <span class="title-rule title-rule--right"></span>
    <span class="title title__line title__line--bottom">LA PRESSE</span>

    <p class="subtitle">A behind-the-scenes journey through<br>the world of book publishing, from<br>manuscript to bookstore.</p>

    <div class="illustration" role="img" aria-label="Closed navy leather-bound book lying on a table with a copper ballpoint pen resting across its cover"></div>

    <span class="author-rule author-rule--left"></span>
    <p class="credits author">LUC VARENNES</p>
    <span class="author-rule author-rule--right"></span>
    <p class="credits publisher">EDITIONS TROVEL</p>
  </main>
</body>
</html>
```